Business card for Full Stable Works Vanhoorne

I would like to have me designed an professional business card with my existing logo for my company called : full stable works vanhoorne gcv.
I prefer a two sided business card with on the back side only the horses head and the website : fswvanhoorne-example.eu
Only one colour shouldbe all right.
The logo must appear in a nic professional way on the business card.

Other suggestion are welcome.

All copy wrights must be released by the designer after we have selected a final design.

Target Market(s)

Equestrian businesses

Industry/Entity Type

Business

Contact Information for Business Card

Gerard Vanhoorne
Title: zaakvoerder
Full Stable Works Vanhoorne GCV
Lindekouter 47
B - 9999 Voorbeeldegem
België
Phone: + 32 400 98 76 10
Mail: gerard@fswvanhoorne-example.eu

Font styles to use
Serif

Requirements
Must have
• My own logo
• See attached files
• Website: fswvanhoorne-example.eu

```html
<!DOCTYPE html>
<html lang="en">
<head>
<meta charset="utf-8">
<title>Full Stable Works Vanhoorne – Business Card</title>
<link href="https://fonts.googleapis.com/css2?family=Open+Sans:wght@400;600;700&display=swap" rel="stylesheet">
<style>
  :root {
    --backdrop: #808080;
    --card-front: #ffffff;
    --card-back: #2a2727;
    --card-back-mark: #1f1d1d;
    --ink: #111111;
    --ink-light: #f2f2f2;
  }
  * { margin: 0; padding: 0; box-sizing: border-box; }
  html, body {
    width: 1200px; height: 900px; overflow: hidden;
    background: var(--backdrop);
    font-family: "Open Sans", Arial, sans-serif;
  }
  .stage { position: relative; width: 1200px; height: 900px; }

  .card { position: absolute; top: 275px; width: 477px; height: 294px; }
  .card-front {
    left: 116px; background: var(--card-front);
    border-radius: 0 52px 0 52px; color: var(--ink);
  }
  .card-back {
    left: 622px; top: 276px; height: 293px; background: var(--card-back);
    border-radius: 52px 0 52px 0;
  }

  .holder-name {
    position: absolute; right: 19px; top: 34px;
    font-size: 17px; font-weight: 600;
  }
  .brand {
    position: absolute; left: 48px; top: 105px;
    display: flex; align-items: center; gap: 9px;
  }
  .brand-dot { width: 22px; height: 22px; border-radius: 50%; background: var(--ink); }
  .brand-name { font-size: 19px; font-weight: 600; color: var(--ink); white-space: nowrap; }

  .contact { position: absolute; right: 21px; top: 205px; text-align: right; font-size: 13px; line-height: 18px; }
  .contact-line { display: flex; justify-content: flex-end; align-items: center; gap: 6px; }
  .contact-line svg { width: 10px; height: 10px; fill: var(--ink); }
  .address { margin-top: 7px; padding-right: 0; }

  .back-mark {
    position: absolute; left: 170px; top: 42px; width: 160px; height: 190px;
    border-radius: 50%; background: var(--card-back-mark);
  }
  .website {
    position: absolute; left: 0; right: 0; top: 251px; text-align: center;
    color: var(--ink-light); font-size: 14px; font-weight: 600;
  }
</style>
</head>
<body>
<div class="stage">
  <section class="card card-front">
    <div class="holder-name">Gerard</div>
    <div class="brand">
      <span class="brand-dot"></span>
      <span class="brand-name">Full Stable Works Vanhoorne</span>
    </div>
    <div class="contact">
      <div class="contact-line">+ 32 400 98 76 10
        <svg viewBox="0 0 24 24"><path d="M6.6 10.8a15 15 0 0 0 6.6 6.6l2.2-2.2c.3-.3.7-.4 1-.2 1.1.4 2.3.6 3.6.6.6 0 1 .4 1 1V20c0 .6-.4 1-1 1A17 17 0 0 1 3 4c0-.6.4-1 1-1h3.5c.6 0 1 .4 1 1 0 1.3.2 2.5.6 3.6.1.3 0 .7-.2 1z"/></svg>
      </div>
      <div class="contact-line">gerard@fswvanhoorne-example.eu
        <svg viewBox="0 0 24 24"><path d="M2 5h20v14H2z M2 5l10 8 10-8" stroke="#fff" stroke-width="1.5"/></svg>
      </div>
      <div class="address">Lindekouter 47, B - 9999 Voorbeeldegem Belgie</div>
    </div>
  </section>

  <section class="card card-back" role="img" aria-label="Dark textured card back with embossed horse head emblem">
    <div class="back-mark"></div>
    <div class="website">www.fswvanhoorne-example.eu</div>
  </section>
</div>
</body>
</html>
```